Bureau for Venture and Discovery Links Needs a Graphically Designed Powerpoint Template

We are from Bureau for Venture and Discovery Links (BVDL), part of a medical school. BVDL contributes to the medical school by overseeing and managing intellectual property generated by researchers at the medical school, and also works to ensure optimal commercial outcomes for all inventions arising from the medical school. We want a graphically designed powerpoint presentation template to describe how BVDL is involved in a researcher’s journey to major scientific contributions. The journey should be represented in the form of a main road (or pathway). Along the main road, there will be smaller roads branching out, each representing one of the researcher’s major scientific contributions. We will be inputting text details of each major scientific contribution near each of the small road branches. The smaller road branches will also need to be removable / editable. This is because we might need to send the template to different researchers to input details of their major scientific contributions, and each researcher will have a different number of them. Hence, you can possibly place around 6 branches along the main road, but we want to be able to remove the branches should we need to. Removal of the branches (design elements) should still result in a seamless image in powerpoint. We also want to be able to add and edit text in the design template. The start of the main road should contain a placeholder for us to place the researcher’s photo. The end of the road will lead to one of the major scientific contributions. Please see the uploaded sketch to have an idea of what we are looking to get. We welcome deviations and changes to the design as shown from the sketch, as long as the design is able to convey what we have described above. As this powerpoint template will be used for presentation to the senior management, we need it to look beautiful yet professional.

Target Market(s)

Researcher, Scientist

Industry/Entity Type

School

Font styles to use
Serif
Sans Serif

Requirements
Must have
• A main road or pathway as mentioned in the project description.
Nice to have
• We will leave the "nice to haves" to be decided by the designer.
Should not have
• Trees

```html
<!DOCTYPE html>
<html lang="en">
<head>
<meta charset="utf-8">
<title>BVDL – Where Are You Going?</title>
<link rel="stylesheet" href="https://fonts.googleapis.com/css2?family=Raleway:wght@300;400;500;700;800&display=swap">
<style>
  :root {
    --bg: #ffffff;
    --band: #6b6b6b;
    --brand-grey: #7a7a7a;
    --road: #5e5e5e;
    --road-line: #ffffff;
    --ink: #1f1f1f;
    --green: #8cc84b;
    --orange: #f08a35;
    --blue: #5a9bd8;
    --photo-ring: #3c6f9c;
    --light-red: #d9483b;
    --light-amber: #f2c230;
    --light-green: #5cb85c;
  }
  * { margin: 0; padding: 0; box-sizing: border-box; }
  html, body { width: 1200px; height: 675px; overflow: hidden; background: var(--bg); }
  body { font-family: "Raleway", "Helvetica Neue", Arial, sans-serif; color: var(--ink); }
  .slide { position: relative; width: 1200px; height: 675px; overflow: hidden; background: var(--bg); }

  .header-band {
    position: absolute; left: 190px; top: 0; width: 1010px; height: 55px;
    background: var(--band);
    display: flex; align-items: center; justify-content: flex-end; padding-right: 30px;
  }
  .slide-title { color: #fff; font-size: 29px; font-weight: 300; letter-spacing: 0.2px; }
  .slide-title strong { font-weight: 700; }

  .brand { position: absolute; color: var(--brand-grey); font-weight: 700; line-height: 1; }
  .brand-name { display: block; }
  .brand-full { display: block; white-space: nowrap; }
  .brand--corner { left: 4px; top: 2px; }
  .brand--corner .brand-name { font-size: 42px; letter-spacing: 2px; }
  .brand--corner .brand-full { font-size: 8.4px; margin-top: 3px; }
  .brand--hub { left: 548px; top: 84px; text-align: center; width: 172px; }
  .brand--hub .brand-name { font-size: 48px; letter-spacing: 3px; }
  .brand--hub .brand-full { font-size: 8.6px; margin-top: 4px; }

  .roadmap { position: absolute; left: 0; top: 0; }

  .label { position: absolute; font-size: 22px; font-weight: 400; line-height: 1.25; }
  .label--center { text-align: center; }
  .researcher-title { left: 22px; top: 230px; width: 120px; text-align: center; font-size: 20px; }
  .contribution--first { left: 98px; top: 458px; width: 190px; }
  .hub-projects { left: 652px; top: 174px; }
  .degree--three { left: 858px; top: 398px; }
  .degree--two { left: 640px; top: 577px; }
  .contribution--end { left: 1024px; top: 470px; width: 170px; text-align: right; }
</style>
</head>
<body>
<div class="slide">
  <div class="brand brand--corner">
    <span class="brand-name">BVDL</span>
    <span class="brand-full">Bureau for Venture and Discovery Links</span>
  </div>
  <header class="header-band">
    <h1 class="slide-title">WHERE <strong>ARE YOU GOING?</strong></h1>
  </header>

  <svg class="roadmap" width="1200" height="675" viewBox="0 0 1200 675" xmlns="http://www.w3.org/2000/svg">
    <defs>
      <linearGradient id="photoTone" x1="0" y1="0" x2="0" y2="1">
        <stop offset="0" stop-color="#d6d6d6"/>
        <stop offset="1" stop-color="#6d6d6d"/>
      </linearGradient>
    </defs>

    <!-- branch roads -->
    <g class="branch-roads" fill="none">
      <g stroke="var(--road)" stroke-width="7">
        <line x1="200" y1="278" x2="200" y2="404"/>
        <line x1="632" y1="278" x2="632" y2="148"/>
        <line x1="720" y1="502" x2="720" y2="628"/>
        <line x1="944" y1="502" x2="944" y2="372"/>
      </g>
      <g stroke="var(--road-line)" stroke-width="1.2" stroke-dasharray="6 4">
        <line x1="200" y1="282" x2="200" y2="402"/>
        <line x1="632" y1="274" x2="632" y2="150"/>
        <line x1="720" y1="506" x2="720" y2="626"/>
        <line x1="944" y1="498" x2="944" y2="374"/>
      </g>
    </g>

    <!-- main road -->
    <g class="main-road" fill="none">
      <path d="M0 278 H696 A56 56 0 0 1 696 390 H504 A56 56 0 0 0 504 502 H1020"
            stroke="var(--road)" stroke-width="9"/>
      <path d="M0 278 H696 A56 56 0 0 1 696 390 H504 A56 56 0 0 0 504 502 H1020"
            stroke="var(--road-line)" stroke-width="1.4" stroke-dasharray="10 5"/>
    </g>

    <!-- crossings -->
    <g class="crossings" fill="var(--road-line)">
      <rect x="190" y="274" width="20" height="1.5"/><rect x="190" y="277" width="20" height="1.5"/><rect x="190" y="280" width="20" height="1.5"/>
      <rect x="622" y="274" width="20" height="1.5"/><rect x="622" y="277" width="20" height="1.5"/><rect x="622" y="280" width="20" height="1.5"/>
      <rect x="534" y="386" width="20" height="1.5"/><rect x="534" y="389" width="20" height="1.5"/><rect x="534" y="392" width="20" height="1.5"/>
      <rect x="710" y="498" width="20" height="1.5"/><rect x="710" y="501" width="20" height="1.5"/><rect x="710" y="504" width="20" height="1.5"/>
      <rect x="934" y="498" width="20" height="1.5"/><rect x="934" y="501" width="20" height="1.5"/><rect x="934" y="504" width="20" height="1.5"/>
    </g>

    <!-- traffic lights -->
    <g class="traffic-light">
      <rect x="616" y="262" width="1.5" height="12" fill="var(--road)"/>
      <rect x="614" y="244" width="6" height="16" rx="1" fill="#555"/>
      <circle cx="617" cy="248" r="1.6" fill="var(--light-red)"/>
      <circle cx="617" cy="252" r="1.6" fill="var(--light-amber)"/>
      <circle cx="617" cy="256" r="1.6" fill="var(--light-green)"/>
    </g>
    <g class="traffic-light">
      <rect x="706" y="484" width="1.5" height="12" fill="var(--road)"/>
      <rect x="704" y="466" width="6" height="16" rx="1" fill="#555"/>
      <circle cx="707" cy="470" r="1.6" fill="var(--light-red)"/>
      <circle cx="707" cy="474" r="1.6" fill="var(--light-amber)"/>
      <circle cx="707" cy="478" r="1.6" fill="var(--light-green)"/>
    </g>

    <!-- institution icon -->
    <g class="icon-institution" fill="var(--green)">
      <polygon points="200,404 226,416 174,416"/>
      <rect x="178" y="418" width="44" height="3"/>
      <rect x="181" y="423" width="5" height="20"/>
      <rect x="190" y="423" width="5" height="20"/>
      <rect x="199" y="423" width="5" height="20"/>
      <rect x="208" y="423" width="5" height="20"/>
      <rect x="216" y="423" width="5" height="20"/>
      <rect x="176" y="445" width="48" height="6"/>
    </g>

    <!-- graduation caps -->
    <g class="icon-cap" fill="var(--orange)">
      <polygon points="944,338 976,349 944,360 912,349"/>
      <path d="M926 354 V364 Q944 374 962 364 V354 L944 361 Z"/>
      <rect x="919" y="350" width="2" height="16"/>
      <rect x="917" y="362" width="6" height="11" rx="1"/>
    </g>
    <g class="icon-cap" fill="var(--blue)">
      <polygon points="720,618 752,629 720,640 688,629"/>
      <path d="M702 634 V644 Q720 654 738 644 V634 L720 641 Z"/>
      <rect x="695" y="630" width="2" height="16"/>
      <rect x="693" y="642" width="6" height="11" rx="1"/>
    </g>

    <!-- researcher photo placeholder -->
    <circle cx="82" cy="166" r="58" fill="url(#photoTone)" role="img" aria-label="Researcher portrait photo"/>
    <circle cx="82" cy="166" r="58" fill="none" stroke="var(--photo-ring)" stroke-width="2.5"/>
  </svg>

  <div class="brand brand--hub">
    <span class="brand-name">BVDL</span>
    <span class="brand-full">Bureau for Venture and Discovery Links</span>
  </div>

  <p class="label researcher-title">MD.PhD</p>
  <p class="label label--center contribution--first">Major Scientific<br>Contribution 1</p>
  <p class="label hub-projects">BVDL XYZ<br>Projects</p>
  <p class="label degree--three">MSc 3</p>
  <p class="label degree--two">MSc 2</p>
  <p class="label contribution--end">Major Scientific<br>Contribution 1</p>
</div>
</body>
</html>
```